Product label design needed for an odor removal line of products.

I need a label designed for an odor removal product line. There are eight additional odor removal products that I will need labels designed for so the winner will have additional work from me. I would like each of those products to have a similar look and feel in each one. This contest is for one of the products. The Odor Eliminator 417 (would love a better name if you are so inclined -many people know what it is by the 417). The no smell formula does not mask odors, it eliminates odors at their source . Also Reduces Allergens! Simply open silver packet and place in dispenser. Great for use in cars, near pet beds or litter boxes, near diaper pails -anywhere odors are a problem. Lasts 60-90 days. Safe to use. Other uses: Nursing homes, hotel rooms, locker rooms, teenage boy rooms, basements... Eco Friendly! No VOC's or phthalates! Do not consume. Keep out of reach of children and pets. Replace every 60-90 days. I put the picture of my logo , the product as it is packaged and a picture of the actual product and the dispenser it will go in. the package is 4x5 in silver packet with .25 seam on the side and .5 seam on the top and bottom. (Dispenser will have a label with reorder information on it. to be designed later) You do not have to put all information provided on the label. It is to be used as you see fit. I tend to like clean, bold designs but am open to all options. Prefer not to use word air freshener.

Target Market(s)

Men and women between 30-65

Industry/Entity Type

Cleaning Product

Font styles to use
Sans Serif

Colors
acd136
9bcb3c
ffffff

Requirements
Must have
• ability for concept/look to be used for a laundry product, smaller odor elimination pouch, odor removing canister and spray as well
Nice to have
• I like greens but am open to designers to decide
Should not have
• word air freshener

```html
<!DOCTYPE html>
<html lang="en">
<head>
<meta charset="utf-8">
<title>417 The Odor Eliminator Label</title>
<link rel="stylesheet" href="https://fonts.googleapis.com/css2?family=Barlow+Semi+Condensed:wght@600&family=Oswald:wght@600&family=Montserrat:wght@500;600&display=swap">
<style>
  :root {
    --green: #86bf2c;
    --green-text: #8cc63f;
    --charcoal: #3b3536;
    --backdrop: #363132;
    --white: #ffffff;
  }
  * { margin: 0; padding: 0; box-sizing: border-box; }
  html, body { width: 1200px; height: 1000px; overflow: hidden; }
  body { background: var(--backdrop); position: relative; font-family: "Oswald", sans-serif; font-weight: 600; }

  .label { position: absolute; left: 190px; top: 55px; width: 819px; height: 889px; background: var(--charcoal); }

  .hero { position: absolute; left: 0; top: 0; width: 819px; height: 349px; background: var(--green); overflow: hidden; }
  .hero-number {
    position: absolute; left: 48px; top: -6px;
    font-family: "Barlow Semi Condensed", sans-serif; font-weight: 600;
    font-size: 330px; line-height: 1; color: var(--white); letter-spacing: -4px;
  }
  .title-line {
    position: absolute; left: 454px; width: 308px; height: 58px;
    display: flex; align-items: center; gap: 6px;
    font-size: 72px; line-height: 58px; color: var(--charcoal); letter-spacing: -1px;
  }
  .title-line .bar { height: 58px; background: var(--charcoal); flex: 1; }
  .title-line.one { top: 58px; }
  .title-line.two { top: 146px; }
  .title-line.three { top: 232px; }

  .claim-band {
    position: absolute; left: 0; top: 349px; width: 819px; height: 84px;
    display: flex; align-items: center; justify-content: center;
    color: var(--white); font-size: 40px; letter-spacing: -1px;
  }

  .uses { position: absolute; left: 0; top: 433px; width: 819px; height: 323px; background: var(--white); }
  .uses-tag {
    position: absolute; left: 47px; width: 167px; height: 67px;
    display: flex; align-items: center; justify-content: center; text-align: center;
    font-size: 30px; line-height: 28px; letter-spacing: -0.5px;
  }
  .uses-tag.primary { top: 67px; background: var(--green); color: var(--white); }
  .uses-tag.secondary { top: 189px; background: var(--charcoal); color: var(--white); }
  .uses-divider { position: absolute; left: 0; top: 0; }

  .use-row { position: absolute; left: 0; width: 819px; height: 60px; }
  .use-row.primary { top: 71px; color: var(--charcoal); }
  .use-row.secondary { top: 193px; color: var(--green-text); }
  .use-item {
    position: absolute; top: 0; height: 60px; transform: translateX(-50%);
    display: flex; align-items: center; text-align: center; white-space: nowrap;
    font-size: 20px; line-height: 22px; letter-spacing: -0.3px;
  }
  .use-sep { position: absolute; top: 16px; width: 2px; height: 30px; }
  .use-row.primary .use-sep { background: var(--green); }
  .use-row.secondary .use-sep { background: var(--charcoal); }

  .footer { position: absolute; left: 0; top: 756px; width: 819px; height: 101px; background: var(--green); }
  .badge { position: absolute; top: 10px; width: 110px; text-align: center; color: var(--white); }
  .badge svg { display: block; margin: 0 auto; }
  .badge-caption { font-family: "Montserrat", sans-serif; font-weight: 600; font-size: 9px; letter-spacing: 0.3px; margin-top: 8px; }

  .maker-mark { position: absolute; left: 637px; top: -44px; width: 88px; height: 88px; border-radius: 50%; background: var(--charcoal); border: 3px solid var(--green); }
  .maker {
    position: absolute; right: 46px; top: 50px; text-align: center; color: var(--white);
    font-family: "Montserrat", sans-serif; font-weight: 500;
  }
  .maker-kicker { font-size: 10px; letter-spacing: 0.5px; color: var(--charcoal); }
  .maker-name { font-size: 18px; letter-spacing: 1.5px; line-height: 22px; }
</style>
</head>
<body>
  <main class="label">
    <section class="hero">
      <div class="hero-number">417</div>
      <div class="title-line one"><span>THE</span><span class="bar"></span></div>
      <div class="title-line two"><span>ODOR</span><span class="bar"></span></div>
      <div class="title-line three"><span>ELIMINATOR</span></div>
    </section>

    <div class="claim-band">THE NO SMELL FORMULA DOES NOT MASK ODORS</div>

    <section class="uses">
      <svg class="uses-divider" width="819" height="323" viewBox="0 0 819 323">
        <polygon points="188,134 214,160 188,160" fill="var(--charcoal)"/>
        <line x1="188" y1="160" x2="773" y2="160" stroke="var(--charcoal)" stroke-width="2"/>
        <polygon points="47,160 75,189 47,189" fill="var(--green)"/>
      </svg>

      <div class="uses-tag primary">GREAT FOR<br>USE IN</div>
      <div class="use-row primary">
        <div class="use-item" style="left:281px">CARS</div>
        <div class="use-sep" style="left:349px"></div>
        <div class="use-item" style="left:415px">NEAR<br>PET BEDS</div>
        <div class="use-sep" style="left:483px"></div>
        <div class="use-item" style="left:550px">NEAR<br>DIAPER PAILS</div>
        <div class="use-sep" style="left:617px"></div>
        <div class="use-item" style="left:712px">ANYWHERE ODOR<br>ARE A PROBLEM</div>
      </div>

      <div class="uses-tag secondary">OTHER<br>USES</div>
      <div class="use-row secondary">
        <div class="use-item" style="left:281px">NURISING<br>HOMES</div>
        <div class="use-sep" style="left:349px"></div>
        <div class="use-item" style="left:415px">HOTEL<br>ROOMS</div>
        <div class="use-sep" style="left:483px"></div>
        <div class="use-item" style="left:550px">LOCKER<br>ROOMS</div>
        <div class="use-sep" style="left:617px"></div>
        <div class="use-item" style="left:712px">TEENAGE BOY<br>ROOMS</div>
      </div>
    </section>

    <footer class="footer">
      <div class="badge" style="left:26px">
        <svg width="58" height="58" viewBox="0 0 58 58" role="img" aria-label="Globe with sprouting leaves icon">
          <circle cx="29" cy="31" r="25" fill="var(--white)"/>
        </svg>
        <div class="badge-caption">ECO FRIENDLY</div>
      </div>
      <div class="badge" style="left:129px">
        <svg width="58" height="58" viewBox="0 0 58 58">
          <circle cx="29" cy="31" r="25" fill="none" stroke="var(--white)" stroke-width="3"/>
          <text x="29" y="29" text-anchor="middle" font-family="Montserrat, sans-serif" font-weight="600" font-size="13" fill="var(--white)">VOC's</text>
          <text x="29" y="43" text-anchor="middle" font-family="Montserrat, sans-serif" font-weight="600" font-size="13" fill="var(--white)">FREE</text>
        </svg>
        <div class="badge-caption">VOC's FREE</div>
      </div>
      <div class="badge" style="left:237px">
        <svg width="58" height="58" viewBox="0 0 58 58">
          <circle cx="29" cy="31" r="25" fill="none" stroke="var(--white)" stroke-width="3"/>
          <text x="29" y="26" text-anchor="middle" font-family="Montserrat, sans-serif" font-weight="600" font-size="5" fill="var(--white)">PHTHALATE</text>
          <text x="29" y="39" text-anchor="middle" font-family="Montserrat, sans-serif" font-weight="600" font-size="13" fill="var(--white)">FREE</text>
        </svg>
        <div class="badge-caption">PHTHALATE FREE</div>
      </div>

      <div class="maker-mark"></div>
      <div class="maker">
        <div class="maker-kicker">PRODUCT OF</div>
        <div class="maker-name">CLEARFIELD HOME</div>
      </div>
    </footer>
  </main>
</body>
</html>
```